Awesome Design for a psychotherapy practise

We need a simple but modern design for a psychotherapy practise which opened recently. A logo, letterhead and a business card. Maybe something with the greek letter psi.

Font styles to use
Serif
Sans Serif

```html
<!DOCTYPE html>
<html lang="en">
<head>
<meta charset="utf-8">
<title>Meridian Therapy – Stationery</title>
<link rel="stylesheet" href="https://fonts.googleapis.com/css2?family=Raleway:wght@300;400&family=Lato:wght@400;700&family=EB+Garamond&family=Oswald:wght@500&display=swap">
<style>
:root{
  --bg:#b8b8b8;
  --paper:#ffffff;
  --paper-soft:#f2f3f3;
  --teal-light:#9de6e8;
  --teal:#2ecfc9;
  --teal-deep:#1fb7a6;
  --ink:#2a2a2a;
  --ink-muted:#5a5a5a;
  --folder:#222222;
  --folder-shade:#2a3a3a;
}
*{margin:0;padding:0;box-sizing:border-box}
html,body{width:1200px;height:1200px;overflow:hidden;background:var(--bg)}
.canvas{position:relative;width:1200px;height:1200px}
.piece{position:absolute;overflow:hidden}

/* brand lockup */
.brand{position:absolute;display:flex;flex-direction:column;align-items:center}
.brand-mark{border-radius:50%;background:var(--teal)}
.brand-name{font-family:'Raleway',sans-serif;font-weight:300;letter-spacing:.06em;color:var(--ink);white-space:nowrap;margin-top:8px}
.brand--light .brand-name{color:#ffffff}
.brand-url{font-family:'Lato',sans-serif;font-weight:700;color:var(--teal);font-size:6.5px;letter-spacing:.04em;margin-top:4px}

.smallcaps{font-family:'Lato',sans-serif;font-variant:small-caps;color:var(--ink-muted)}
.social{position:absolute;display:flex;gap:3px}
.social span{display:block;width:9px;height:9px;border-radius:2px;background:var(--ink)}
.social--light span{background:#ffffff}

/* letterhead */
.letterhead{left:14px;top:144px;width:446px;height:630px;background:var(--paper)}
.letterhead .band-top{position:absolute;left:208px;top:38px;width:238px;height:60px;background:var(--teal-light)}
.letterhead .sender{position:absolute;left:327px;top:126px;font-size:7.5px;line-height:9px}
.letterhead .sender p{margin-bottom:7px}
.letterhead .recipient{position:absolute;left:42px;top:170px;font-size:8.5px;line-height:11px}
.letterhead .title{position:absolute;left:0;width:100%;top:278px;text-align:center;font-family:'Oswald',sans-serif;font-weight:500;font-size:13px;color:var(--ink)}
.letterhead .body{position:absolute;left:42px;top:302px;width:376px;font-family:'EB Garamond',serif;font-size:7.6px;line-height:8.6px;color:var(--ink);text-align:justify}
.letterhead .body p{text-indent:28px;margin-bottom:8px}
.letterhead .body p.tight{margin-bottom:0}
.letterhead .signoff{position:absolute;left:70px;top:464px;font-family:'EB Garamond',serif;font-size:7.6px;line-height:8.6px;color:var(--ink)}
.letterhead .footer{position:absolute;left:0;top:520px;width:100%;height:86px;background:var(--paper-soft)}
.letterhead .footer-mark{position:absolute;left:92px;top:8px;width:80px;height:80px;border-radius:50%;background:#ffffff}
.letterhead .band-bottom{position:absolute;left:0;top:606px;width:100%;height:24px;background:var(--teal-light)}

/* folder */
.folder{left:510px;top:144px;width:446px;height:630px;background:var(--folder)}
.folder .spine{position:absolute;left:0;top:0;width:28px;height:100%;background:#1b1b1b}
.folder .watermark{position:absolute;left:60px;top:360px;width:300px;height:300px;border-radius:50%;background:var(--folder-shade);opacity:.8}

/* business cards */
.card{width:192px;height:107px;background:var(--paper-soft)}
.card-front{left:15px;top:826px}
.card-back{left:15px;top:952px}
.card-back .holder{position:absolute;left:67px;top:12px;font-family:'Lato',sans-serif;font-variant:small-caps;font-weight:700;font-size:12px;color:var(--ink-muted)}
.card-back .panel{position:absolute;left:68px;top:29px;width:113px;height:68px;background:var(--teal-light);padding:6px 5px;font-family:'Lato',sans-serif;color:#ffffff}
.card-back .phone{font-size:8px;font-weight:700;line-height:10px}
.card-back .line{font-size:5px;font-weight:700;line-height:7px;margin-top:2px}

/* envelopes */
.envelope{width:446px;height:210px;background:var(--paper-soft)}
.envelope-front{left:256px;top:840px}
.envelope-front .watermark{position:absolute;left:230px;top:-20px;width:70px;height:70px;border-radius:50%;background:var(--teal-light);opacity:.35}
.envelope-front .band{position:absolute;left:0;top:100px;width:100%;height:76px;background:var(--teal-light)}
.envelope-front .window{position:absolute;left:264px;top:91px;width:160px;height:90px;border-radius:10px;background:#ffffff}
.envelope-front .contact{position:absolute;left:14px;top:106px;font-family:'Lato',sans-serif;color:#ffffff;font-size:3.8px;line-height:8px}
.envelope-back{left:746px;top:840px}
.envelope-back .flap{position:absolute;left:0;top:0;width:100%;height:64px;background:#f7f8f8;clip-path:polygon(0 0,100% 0,96% 100%,4% 100%)}
.envelope-back .band-left{position:absolute;left:0;top:82px;width:138px;height:75px;background:var(--teal-light)}
.envelope-back .band-right{position:absolute;right:0;top:82px;width:138px;height:75px;background:var(--teal-light)}
</style>
</head>
<body>
<main class="canvas">

  <!-- Letterhead -->
  <section class="piece letterhead">
    <div class="band-top"></div>
    <div class="brand" style="left:42px;top:30px;width:140px">
      <div class="brand-mark" style="width:62px;height:62px"></div>
      <div class="brand-name" style="font-size:13px;margin-top:28px">MERIDIAN THERAPY</div>
    </div>
    <div class="sender smallcaps">
      <p>1420 Harbor Lane<br>Suite 210, Eastfield, CA<br>90112</p>
      <p>Office 555.201.4410<br>Cell&nbsp;&nbsp;555.201.7720</p>
      <p>office@meridiantherapy.com<br>www.meridiantherapy.com</p>
    </div>
    <div class="recipient smallcaps">
      Luly, 22, 2021<br>Dear<br>Mr. Alan Reed<br>Creative<br>director<br>London, GB
    </div>
    <h1 class="title">Title</h1>
    <div class="body">
      <p>Tempor sunt magna consequat ullamco. Amet excepteur, incididunt nulla est tempor officia magna ea sunt ut eu velit mollit:</p>
      <p>Ut, magna reprehenderit. Dolor deserunt do sit amet laboris do qui velit, officia deserunt proident fugiat ea aliqua tempor, ea non? Ut eu, culpa, officia, duis aliqua ea, elit pariatur qui ex, nisi aute et esse tempor, non proident.</p>
      <p class="tight">Ad officia voluptate enim aute pariatur ex laboris ut. Et ut consequat cupidatat reprehenderit do ut pariatur. Commodo incididunt occaecat pariatur, anim ex.</p>
      <p>Exercitation, sed id in dolor: Magna consectetur ad aliquip ex proident dolor velit sit est pariatur ut. Incididunt ut officia est cupidatat occaecat ea adipisicing ut cupidatat.</p>
      <p>Esse aliqua, velit pariatur ea magna proident pariatur consequat ad ut do tempor ea, consectetur qui excepteur dolor. Pariatur aliquip, minim nostrud exercitation sint ullamco elit. Magna sed dolor minim fugiat in ullamco, nulla ut nisi esse commodo ut enim? Et cupidatat enim consequat lorem in ipsum consequat id aliquip fugiat aute nulla culpa non.</p>
    </div>
    <div class="signoff">Best regards<br><br>Name Surname<br>any text</div>
    <div class="footer"><div class="footer-mark"></div></div>
    <div class="social" style="left:390px;top:590px"><span></span><span></span><span></span></div>
    <div class="band-bottom"></div>
  </section>

  <!-- Folder cover -->
  <section class="piece folder">
    <div class="spine"></div>
    <div class="watermark"></div>
    <div class="brand brand--light" style="left:250px;top:245px;width:150px">
      <div class="brand-mark" style="width:58px;height:58px"></div>
      <div class="brand-name" style="font-size:14px;margin-top:22px">MERIDIAN THERAPY</div>
    </div>
    <div class="social social--light" style="left:24px;top:492px"><span></span><span></span><span></span></div>
  </section>

  <!-- Business card front -->
  <section class="piece card card-front">
    <div class="brand" style="left:0;top:12px;width:192px">
      <div class="brand-mark" style="width:48px;height:48px"></div>
      <div class="brand-name" style="font-size:11px;margin-top:14px">MERIDIAN THERAPY</div>
      <div class="brand-url">WWW.MERIDIANTHERAPY.COM</div>
    </div>
  </section>

  <!-- Business card back -->
  <section class="piece card card-back">
    <div class="brand" style="left:6px;top:28px;width:56px">
      <div class="brand-mark" style="width:22px;height:22px"></div>
      <div class="brand-name" style="font-size:5px;margin-top:6px;font-weight:400">MERIDIAN THERAPY</div>
    </div>
    <div class="social" style="left:20px;top:75px"><span></span><span></span><span></span></div>
    <div class="holder">Name Surname</div>
    <div class="panel">
      <div class="phone">555.201.4410<br>555.201.7720</div>
      <div class="line">OFFICE@MERIDIANTHERAPY.COM</div>
      <div class="line" style="font-variant:small-caps">1420 Harbor Lane<br>Suite 210, Eastfield, CA<br>90112</div>
    </div>
  </section>

  <!-- Envelope front -->
  <section class="piece envelope envelope-front">
    <div class="watermark"></div>
    <div class="band"></div>
    <div class="window"></div>
    <div class="brand" style="left:14px;top:18px;width:140px">
      <div class="brand-mark" style="width:52px;height:52px"></div>
      <div class="brand-name" style="font-size:11.5px;margin-top:10px">MERIDIAN THERAPY</div>
    </div>
    <div class="contact">
      1420 Harbor Lane, Suite 210, Eastfield, CA 90112<br>
      Office 555.201.4410 · Cell 555.201.7720<br>
      office@meridiantherapy.com<br>
      www.meridiantherapy.com
    </div>
    <div class="social social--light" style="left:14px;top:150px"><span style="width:5px;height:5px"></span><span style="width:5px;height:5px"></span><span style="width:5px;height:5px"></span></div>
  </section>

  <!-- Envelope back -->
  <section class="piece envelope envelope-back">
    <div class="flap"></div>
    <div class="band-left"></div>
    <div class="band-right"></div>
    <div class="brand" style="left:148px;top:84px;width:150px">
      <div class="brand-mark" style="width:52px;height:52px"></div>
      <div class="brand-name" style="font-size:11.5px;margin-top:10px">MERIDIAN THERAPY</div>
      <div class="brand-url">WWW.MERIDIANTHERAPY.COM</div>
    </div>
  </section>

</main>
</body>
</html>
```